Name card design for KOV mobile accessories company

KOV is an upmarket brand, we are looking for professional business card design.

the design should be neat and simple but giving a strong feeling.
should not be colorful. make it black/white/gray tone

Name:
Job title:
Contact no.:
company address: i would like the company address to be very small and thin.
link to social media profile:
company website:

*the company have no website yet
as the project is done please i also would like the font that use in design as well; for more further people in company need a business card:)
Updates

Thank you for all super fast submission :D they're all look cool!

i have just update my brief to make the statement clearer, please check it out :)
if you have any question please dont hesitate to ask.
i would like see more design from you! 
Keep it up!  :D

Target Market(s)

Company target are upmarket company distributor, such as Vordane and Pilto store.

Industry/Entity Type

Business

Font styles to use
Serif
Sans Serif
Other font styles liked:
• Formal and mordern

Colors
ffffff
eeeeee
d3d3d3
919191
474747
1b1b1b
000000
333333

Requirements
Must have
• The design must be professional clean and clear but also Strong and Modern!
text should be formal and mordern
Should not have
• No complicated design!

```html
<!DOCTYPE html>
<html lang="en">
<head>
<meta charset="utf-8">
<title>KOV Business Card</title>
<link rel="stylesheet" href="https://fonts.googleapis.com/css2?family=Open+Sans:wght@300;400&display=swap">
<style>
  :root {
    --page-bg: #eeeeee;
    --card-bg: #d3d3d3;
    --card-edge: #c4c4c4;
    --ink-dark: #333333;
    --ink-mid: #474747;
    --ink-soft: #919191;
    --ink-faint: #e4e4e4;
  }
  * { margin: 0; padding: 0; box-sizing: border-box; }
  html, body {
    width: 1200px;
    height: 900px;
    overflow: hidden;
    background: var(--page-bg);
    font-family: "Open Sans", sans-serif;
  }
  .canvas {
    position: relative;
    width: 1200px;
    height: 900px;
  }
  .card {
    position: absolute;
    left: 320px;
    width: 560px;
    height: 320px;
    background: var(--card-bg);
    box-shadow: 0 2px 0 var(--card-edge), 0 10px 24px rgba(0,0,0,0.12);
  }
  .card-front { top: 90px; }
  .card-back { top: 470px; }

  .brand-mark {
    position: absolute;
    left: 50%;
    top: 50%;
    transform: translate(-50%, -50%);
    display: flex;
    align-items: center;
    gap: 14px;
    color: var(--ink-dark);
    font-weight: 400;
    font-size: 64px;
    letter-spacing: 10px;
    line-height: 1;
  }
  .brand-square {
    width: 18px;
    height: 18px;
    background: var(--ink-dark);
  }

  .brand-watermark {
    position: absolute;
    left: 48px;
    top: 118px;
    color: var(--ink-faint);
    font-weight: 400;
    font-size: 72px;
    letter-spacing: 12px;
    line-height: 1;
  }

  .contact-person {
    position: absolute;
    left: 330px;
    top: 44px;
    color: var(--ink-dark);
    font-size: 13px;
    line-height: 1.35;
  }
  .person-name {
    font-size: 17px;
    letter-spacing: 0.5px;
    text-transform: uppercase;
  }
  .person-phone .phone-label { margin-right: 6px; }

  .office-address {
    position: absolute;
    left: 380px;
    top: 184px;
    color: var(--ink-mid);
    font-weight: 300;
    font-size: 11px;
    line-height: 1.5;
  }

  .online-links {
    position: absolute;
    left: 40px;
    bottom: 34px;
    color: var(--ink-dark);
    font-size: 13px;
    line-height: 1.5;
  }
  .social-line {
    display: flex;
    align-items: center;
    gap: 8px;
  }
  .social-square {
    width: 12px;
    height: 12px;
    background: var(--ink-dark);
    border-radius: 2px;
  }
</style>
</head>
<body>
<main class="canvas">
  <section class="card card-front" aria-label="Card front">
    <div class="brand-mark"><span class="brand-square"></span>KOV</div>
  </section>

  <section class="card card-back" aria-label="Card back">
    <div class="brand-watermark" aria-hidden="true">KOV</div>

    <div class="contact-person">
      <p class="person-name">Daren Holt</p>
      <p class="person-title">Founder &amp; CEO</p>
      <p class="person-phone"><span class="phone-label">M</span>555-014-2290</p>
    </div>

    <address class="office-address" style="font-style: normal;">
      1180 Harbor Plaza, Suite 410,<br>
      Lakeview, MI 49020
    </address>

    <div class="online-links">
      <p class="social-line"><span class="social-square"></span>/kov-mobile</p>
      <p class="website">www.kov-mobile.com</p>
    </div>
  </section>
</main>
</body>
</html>
```